Business Card Design Project

We are a distribution company providing goods to Latin America. We sell everything from Medical equipment, generic medicines, to carecliners. The logo that we use is attached. The logo can incorporate different colors other than black for versatility. The company name is Valdoria International Corporation and/or VIC. The card will be printed using 1 or more of the following: Silk mounted and/or embossed. So if the design ideas could be made to incorporate that technique or any other unique techniques, it would be great. The target market is dialysis centers/doctors.

Basic Info for card:
Marnie Dowsett
Purchasing Manager
555-317-4086 direct
555-241-7953 fax
marnie.dowsett@valdoriavic.example
www.valdoriavic.example

Target Market(s)

Latin America

Industry/Entity Type

Business

Requirements
Nice to have
• The Front of the card should have the basic contact information with company name/logo. The back of the card could incorporate

```html
<!DOCTYPE html>
<html lang="en">
<head>
<meta charset="utf-8">
<title>Valdoria International Corporation — Business Cards</title>
<link rel="stylesheet" href="https://fonts.googleapis.com/css2?family=Source+Sans+3:wght@400;600;700&display=swap">
<style>
  :root {
    --page-bg: #ffffff;
    --ink: #ffffff;
    --violet-light: #a232f5;
    --violet-deep: #4410b8;
    --blue-light: #3576ff;
    --blue-deep: #0a26a3;
    --red-light: #ff1212;
    --red-deep: #8c1020;
  }
  * { box-sizing: border-box; margin: 0; padding: 0; }
  html, body {
    width: 1200px; height: 1200px; overflow: hidden;
    background: var(--page-bg);
  }
  body {
    position: relative;
    font-family: "Source Sans 3", "Myriad Pro", sans-serif;
    color: var(--ink);
  }
  .card {
    position: absolute;
    width: 594px; height: 338px;
    overflow: hidden;
  }
  .card--front { left: 0; }
  .card--back  { left: 606px; }
  .row-1 { top: 46px; }
  .row-2 { top: 409px; }
  .row-3 { top: 779px; height: 339px; }

  .theme-violet { --c1: var(--violet-light); --c2: var(--violet-deep); }
  .theme-blue   { --c1: var(--blue-light);   --c2: var(--blue-deep); }
  .theme-red    { --c1: var(--red-light);    --c2: var(--red-deep); }

  .card--front { background: radial-gradient(ellipse 70% 75% at 58% 45%, var(--c1) 0%, var(--c2) 100%); }
  .card--back  { background: radial-gradient(ellipse 75% 80% at 40% 45%, var(--c1) 0%, var(--c2) 100%); }

  /* Front */
  .brand-mark {
    position: absolute;
    left: 154px; top: 40px; width: 296px; height: 232px;
    display: flex; align-items: center; justify-content: center;
    gap: 16px;
  }
  .brand-mark__dot {
    width: 34px; height: 34px; border-radius: 50%;
    background: var(--ink);
  }
  .brand-mark__name {
    font-weight: 700; font-size: 120px; line-height: 1; letter-spacing: 2px;
  }
  .front-rule {
    position: absolute; left: 154px; top: 281px;
    width: 296px; height: 1.5px; background: var(--ink);
  }
  .front-caption {
    position: absolute; left: 154px; top: 285px; width: 296px;
    text-align: center; font-size: 18px; line-height: 21px; font-weight: 400;
  }

  /* Back */
  .back-mark {
    position: absolute; left: 60px; top: 54px; width: 162px; height: 120px;
    display: flex; align-items: center; justify-content: center;
  }
  .back-mark__name { font-weight: 700; font-size: 64px; line-height: 1; letter-spacing: 1px; }
  .company-name {
    position: absolute; left: 60px; top: 184px;
    font-weight: 700; font-size: 25px; line-height: 30px;
  }
  .divider {
    position: absolute; left: 240px; top: 48px;
    width: 1.5px; height: 228px; background: var(--ink);
  }
  .contact {
    position: absolute; left: 264px; top: 79px; width: 316px;
    font-size: 18px; line-height: 29px; font-weight: 400;
    list-style: none; white-space: nowrap;
  }
  .contact__name { font-weight: 700; font-size: 23px; }
  .contact__title { margin-bottom: 4px; }
</style>
</head>
<body>

  <!-- Violet set -->
  <section class="card card--front theme-violet row-1">
    <div class="brand-mark"><span class="brand-mark__dot"></span><span class="brand-mark__name">VIC</span></div>
    <div class="front-rule"></div>
    <p class="front-caption">Valdoria International Corporation<br>Boston, MA&nbsp; USA</p>
  </section>
  <section class="card card--back theme-violet row-1">
    <div class="back-mark"><span class="back-mark__name">VIC</span></div>
    <p class="company-name">Valdoria<br>International<br>Corporation</p>
    <div class="divider"></div>
    <ul class="contact">
      <li class="contact__name">Marnie Dowsett</li>
      <li class="contact__title">Purchasing Manager</li>
      <li>555-317-4086 direct</li>
      <li>555-241-7953 fax</li>
      <li>marnie.dowsett@valdoriavic.example</li>
      <li>www.valdoriavic.example</li>
    </ul>
  </section>

  <!-- Blue set -->
  <section class="card card--front theme-blue row-2">
    <div class="brand-mark"><span class="brand-mark__dot"></span><span class="brand-mark__name">VIC</span></div>
    <div class="front-rule"></div>
    <p class="front-caption">Valdoria International Corporation<br>Boston, MA&nbsp; USA</p>
  </section>
  <section class="card card--back theme-blue row-2">
    <div class="back-mark"><span class="back-mark__name">VIC</span></div>
    <p class="company-name">Valdoria<br>International<br>Corporation</p>
    <div class="divider"></div>
    <ul class="contact">
      <li class="contact__name">Marnie Dowsett</li>
      <li class="contact__title">Purchasing Manager</li>
      <li>555-317-4086 direct</li>
      <li>555-241-7953 fax</li>
      <li>marnie.dowsett@valdoriavic.example</li>
      <li>www.valdoriavic.example</li>
    </ul>
  </section>

  <!-- Red set -->
  <section class="card card--front theme-red row-3">
    <div class="brand-mark"><span class="brand-mark__dot"></span><span class="brand-mark__name">VIC</span></div>
    <div class="front-rule"></div>
    <p class="front-caption">Valdoria International Corporation<br>Boston, MA&nbsp; USA</p>
  </section>
  <section class="card card--back theme-red row-3">
    <div class="back-mark"><span class="back-mark__name">VIC</span></div>
    <p class="company-name">Valdoria<br>International<br>Corporation</p>
    <div class="divider"></div>
    <ul class="contact">
      <li class="contact__name">Marnie Dowsett</li>
      <li class="contact__title">Purchasing Manager</li>
      <li>555-317-4086 direct</li>
      <li>555-241-7953 fax</li>
      <li>marnie.dowsett@valdoriavic.example</li>
      <li>www.valdoriavic.example</li>
    </ul>
  </section>

</body>
</html>
```